Geschäftspapiere für Immobilienmakler
Tolles Design. Schnelle Umsetzung der Änderungswünsche.
Zielgruppe
Wir sind Immobilienmakler und bieten zusätzlich Home Staging an.
https://nordhaus-kellwang.de/Home-Staging/
Um anderen Immobilienmakler oder Privatanbieter unsere Dienstleistung anzubieten, möchten wir ein Anschreiben gestalten lassen. Welches wir hauptsächlich per E-Mail versenden können, da die Postanschrift oft nicht bekannt ist.
Trotzdem bitte auch eine Rückseite gestalten für den Versand per Post.
Aufgabenstellung
Im Anhang ist ein Muster mit Mustertext.
Bitte auch eine Rückseite gestalten für den Versand per Post.
Das Anschreiben/der Infobrief sollte ansprechend schick aussehen.
Ich könne mir vorstellen, dass oben auf der Seite die gleichen Bilder sind wir auf der Homepage.
Oder dies in den Hintergrund miteingearbeitet wird.
(die Lampe, das Bett, die Badezimmerdeko)
Wichtig ist auch dass das Logo mit der Glühbirne, dem Vogel und dem Slogan 'Ins richtige Licht rücken - Werte steigern'
Weiterhin wichtig dass die Vorher-Nachher Bilder gut zur Geltung kommen.
Ich habe als Datei unsere Flyer und eine Mappe zur Ansicht mit angehängt.
Hier sollte es dazu passen.

```html
<!DOCTYPE html>
<html lang="de">
<head>
<meta charset="utf-8">
<title>Nordhaus Kellwang – Anschreiben Home Staging</title>
<link href="https://fonts.googleapis.com/css2?family=Fira+Sans:wght@500;600;700&family=Tinos:wght@400;700&family=Arimo:wght@400&display=swap" rel="stylesheet">
<style>
:root{
  --navy:#0c4375;
  --gold:#b8913a;
  --paper:#ffffff;
  --stage:#c9c9c9;
  --ink:#1b1b1b;
}
*{box-sizing:border-box;margin:0;padding:0}
html,body{width:1111px;height:1200px;overflow:hidden;background:var(--stage)}
.canvas{position:relative;width:1111px;height:1200px}
.sheet{position:absolute;top:218px;width:540px;height:764px;background:var(--paper);overflow:hidden;box-shadow:0 6px 18px rgba(0,0,0,.25)}
.sheet--front{left:10px}
.sheet--back{left:561px}
.brand{position:absolute;display:flex;align-items:center;gap:7px;font-family:"Fira Sans",sans-serif;font-weight:700;color:var(--navy);font-size:17px;letter-spacing:.2px;white-space:nowrap}
.brand__dot{width:12px;height:12px;border-radius:50%;background:var(--gold)}
.sheet--front .brand--head{right:38px;top:60px}
.sheet--front .brand--foot{right:22px;top:732px;font-size:14px;gap:6px}
.sheet--front .brand--foot .brand__dot{width:10px;height:10px}
.rule{position:absolute;height:2px;background:var(--gold)}
.letter{font-family:"Tinos",serif;color:var(--ink);font-size:8.6px;line-height:12.8px}
.sender{position:absolute;left:74px;top:156px;font-family:"Arimo",sans-serif;font-size:5.2px;color:var(--navy);text-decoration:underline;letter-spacing:-.1px}
.recipient{position:absolute;left:74px;top:171px;font-family:"Arimo",sans-serif;font-size:8px;line-height:11px;color:var(--ink)}
.block{position:absolute;left:74px;width:345px}
.letter b{font-weight:700}
.showcase{position:absolute;left:0;top:446px;width:540px;height:92px;background:var(--navy)}
.photo{position:absolute}
.photo--before{left:138px;top:6px;width:112px;height:77px;background:linear-gradient(180deg,#eef1ec 0%,#c8d3c0 45%,#a27c4d 60%,#8a6437 100%)}
.photo--after{left:292px;top:6px;width:112px;height:77px;background:linear-gradient(180deg,#eef1ec 0%,#c9d4c2 45%,#a8865a 60%,#7e6d6a 78%,#b9b4ae 100%)}
.showcase__arrow{position:absolute;left:242px;top:46px}
.showcase__title{position:absolute;left:27px;top:52px;font-family:"Fira Sans",sans-serif;font-weight:500;color:#fff;font-size:13px}
.showcase__tag{position:absolute;left:0;width:162px;height:22px;background:var(--gold);color:#fff;font-family:"Fira Sans",sans-serif;font-weight:500;font-size:13px;line-height:22px;padding-left:26px}
.footer-contact{position:absolute;top:715px;font-family:"Fira Sans",sans-serif;font-weight:600;color:var(--navy);font-size:8.6px;line-height:11px}
.band{position:absolute;left:308px;top:0;width:232px;height:764px;background:var(--navy)}
.sheet--back .brand{left:332px;top:96px;color:#fff;font-size:16px}
.ref-photo{position:absolute;left:16px;width:200px;height:150px}
.ref-photo--bedroom{top:168px;background:linear-gradient(180deg,#f1f1f1 0%,#d9d7d3 55%,#8f8a86 80%,#6f6b68 100%)}
.ref-photo--lamp{top:330px;background:radial-gradient(circle at 45% 30%,#f7d06a 0%,#d1a23e 30%,#a9a9a6 65%,#e2e2e0 100%)}
.ref-photo--bath{top:492px;background:linear-gradient(180deg,#fafafa 0%,#e8e6e8 55%,#b8a2bd 85%,#c9c2cb 100%)}
.ref-note{position:absolute;left:330px;top:668px;color:#fff;font-family:"Fira Sans",sans-serif;font-weight:600;font-size:9px}
.ref-link{position:absolute;left:326px;top:684px;width:190px;height:24px;background:var(--gold);color:#fff;font-family:"Fira Sans",sans-serif;font-weight:600;font-size:10.5px;line-height:24px;text-align:center}
</style>
</head>
<body>
<div class="canvas">

  <section class="sheet sheet--front">
    <div class="rule" style="left:74px;top:91px;width:298px"></div>
    <div class="brand brand--head"><span class="brand__dot"></span>Nordhaus Kellwang</div>

    <p class="sender">NORDHAUS KELLWANG IMMOBILIEN GMBH | LINDENWEG 14 | 74000 FELDBACH</p>
    <p class="recipient">Firma<br>Ansprechpartner<br>Straße Nummer<br>123456 Ort</p>

    <div class="letter">
      <p class="block" style="top:276px">Sehr geehrter Herr&nbsp;&nbsp;&nbsp;&nbsp;&nbsp;&nbsp;&nbsp;&nbsp;&nbsp;&nbsp;&nbsp;&nbsp;&nbsp;&nbsp;&nbsp;&nbsp;&nbsp;&nbsp;&nbsp;&nbsp;&nbsp;&nbsp;&nbsp;&nbsp;&nbsp;&nbsp;&nbsp;&nbsp;&nbsp;&nbsp;,</p>
      <p class="block" style="top:301px">bei Marktrecherchen ist unserem Backoffice aufgefallen dass wir Ihre Immobilie/Immobilien durch unsere verkaufsfördernden Maßnahmen in ein besseres Licht rücken können.<br><b>Für einen erfolgreichen und schnelleren Verkauf bieten wir HOME STAGING an.</b></p>
      <p class="block" style="top:348px"><b>Was ist HOME STAGING?</b><br>HOME STAGING wird das professionelle herrichten von Räumen oder ganzen Immobilie zur Verkaufsförderung genannt. Diese Adaption umfasst den gezielten Einsatz von Möbeln, Dekoration, Farbe, Licht, Wand- und Fußbodengestaltung.<br>Immobilien, die mit HOME STAGING für den Verkauf vorbereitet werden, haben eine viel kürzere Verkaufszeit und einen <b>höheren Verkaufspreis um ca. 10-15%.</b></p>
      <p class="block" style="top:431px">Hier nur ein Beispiel:</p>
    </div>

    <div class="showcase">
      <div class="photo photo--before" role="img" aria-label="Leeres Wohnzimmer vor dem Home Staging"></div>
      <svg class="showcase__arrow" width="48" height="22" viewBox="0 0 48 22">
        <path d="M3 18 Q20 4 40 10" fill="none" stroke="#fff" stroke-width="3" stroke-linecap="round"/>
        <path d="M34 4 L44 11 L33 15 Z" fill="#fff"/>
      </svg>
      <div class="photo photo--after" role="img" aria-label="Eingerichtetes Wohnzimmer nach dem Home Staging"></div>
      <p class="showcase__title">Vor und nach</p>
    </div>
    <p class="showcase__tag" style="top:524px">dem Home Staging</p>

    <div class="letter">
      <p class="block" style="top:553px"><b>Probieren Sie es aus!</b></p>
      <p class="block" style="top:578px">Anschließend werden Sie jede Immobilie Home Stagen lassen. Gerne machen wir Ihnen ein unschlagbares Kennenlern-Angebot.</p>
      <p class="block" style="top:619px"><b>Mit freundlichen Grüßen<br>Jana und Paul Kellwang</b></p>
      <p class="block" style="top:684px">Weitere Infos unter: www.nordhaus-kellwang.de</p>
    </div>

    <div class="rule" style="left:0;top:700px;width:540px"></div>

    <p class="footer-contact" style="left:74px">Nordhaus Kellwang<br>Immobilien GmbH<br>Lindenweg 14<br>74000 Feldbach</p>
    <p class="footer-contact" style="left:175px;top:726px">Tel.: 0 12 34 / 56 78 90<br>Fax: 0 12 34 / 56 78 91<br>kontakt@nordhaus-kellwang.de</p>

    <div class="brand brand--foot"><span class="brand__dot"></span>Nordhaus Kellwang</div>
  </section>

  <section class="sheet sheet--back">
    <div class="rule" style="left:0;top:112px;width:322px"></div>
    <div class="band">
      <div class="ref-photo ref-photo--bedroom" role="img" aria-label="Gestaltetes Schlafzimmer mit Bett und Spiegel"></div>
      <div class="ref-photo ref-photo--lamp" role="img" aria-label="Goldene Hängelampe in Nahaufnahme"></div>
      <div class="ref-photo ref-photo--bath" role="img" aria-label="Helles Badezimmer mit Dekoration"></div>
    </div>
    <div class="brand"><span class="brand__dot"></span>Nordhaus Kellwang</div>
    <div class="rule" style="left:0;top:695px;width:326px"></div>
    <p class="ref-note">weitere Referenzen finden Sie unter:</p>
    <p class="ref-link">www.nordhaus-kellwang.de</p>
  </section>

</div>
</body>
</html>
```